FR banner

we need a banner design (36"x120" horizontal) that will be displayed on a local high school baseball field. My company ( Crestwell Prints Co) has been producing signage for the Fernmoor Ridge community since 2009. We would like to communicate that we do more than banners. The final design should include the slogan "Signs Shirts Swag" and our Logo.

Target Market(s)

companies, teams, events, shirt and other marketing items.

Industry/Entity Type

Sign, Print,

Font styles to use
Sans Serif

Requirements
Should not have
• no baseball content.

```html
<!DOCTYPE html>
<html lang="en">
<head>
<meta charset="utf-8">
<title>Crestwell Prints Co — Field Banner</title>
<link href="https://fonts.googleapis.com/css2?family=Poppins:wght@400;500;600;700&family=Roboto+Slab:wght@700;800;900&family=Roboto:wght@700;900&display=swap" rel="stylesheet">
<style>
  :root {
    --stage: #484848;
    --concrete-light: #e8e8e8;
    --concrete-mid: #c6c6c6;
    --ink: #1b1b1b;
    --charcoal: #333333;
    --navy-deep: #06122a;
    --navy: #163766;
    --royal: #0b3aa0;
    --sky: #a9c6dc;
    --red: #c81818;
    --red-dark: #7e0d0d;
    --paper: #eeeeee;
    --white: #ffffff;
    --rule: rgba(255,255,255,0.45);
  }
  * { margin: 0; padding: 0; box-sizing: border-box; }
  html, body { width: 1200px; height: 630px; overflow: hidden; }
  body { background: var(--stage); position: relative; font-family: "Poppins", sans-serif; }

  .banner {
    position: absolute; left: 75px; top: 158px; width: 1051px; height: 314px;
    overflow: hidden;
    box-shadow: 0 10px 22px rgba(0,0,0,0.45);
    background: radial-gradient(ellipse at 30% 45%, var(--concrete-light) 0%, var(--concrete-mid) 85%);
  }
  .navy-field {
    position: absolute; right: 0; top: 0; width: 598px; height: 100%;
    background: radial-gradient(ellipse at 65% 40%, var(--navy) 0%, var(--navy-deep) 85%);
  }
  .reveal {
    position: absolute; left: 300px; top: 34px; width: 450px; height: 262px;
    border-radius: 46% 40% 44% 38% / 40% 48% 42% 50%;
    background: radial-gradient(ellipse at 50% 50%, var(--red) 0%, var(--red-dark) 100%);
    box-shadow: 0 0 0 10px var(--paper);
  }

  /* Brand block */
  .brand {
    position: absolute; left: 36px; top: 78px;
    display: flex; align-items: center; gap: 12px;
  }
  .brand-dot { width: 30px; height: 30px; border-radius: 50%; background: var(--charcoal); flex: none; }
  .brand-text { display: flex; flex-direction: column; }
  .brand-name {
    font-family: "Roboto", sans-serif; font-weight: 900; font-size: 30px; line-height: 1.02;
    color: var(--charcoal); text-transform: uppercase;
  }
  .brand-est {
    align-self: flex-end; margin-top: 6px;
    font-size: 9px; color: var(--charcoal); font-weight: 600;
  }

  .social {
    position: absolute; left: 36px; top: 229px; display: flex; align-items: center; gap: 7px;
    font-size: 19px; font-weight: 500; color: var(--ink); white-space: nowrap;
  }
  .social-dot { width: 17px; height: 17px; border-radius: 50%; background: var(--royal); }
  .social-handle { color: var(--royal); }

  .order-bar {
    position: absolute; left: 31px; top: 264px; width: 455px; height: 28px;
    display: flex; border-radius: 7px; overflow: hidden; border: 1px solid var(--royal);
  }
  .order-label {
    width: 164px; background: var(--sky); color: var(--ink);
    font-weight: 600; font-size: 14px; letter-spacing: 1.2px;
    display: flex; align-items: center; justify-content: center;
  }
  .order-url {
    flex: 1; background: var(--royal); color: var(--white);
    font-weight: 500; font-size: 15.5px; letter-spacing: 1.6px;
    display: flex; align-items: center; justify-content: center;
  }

  /* Slogan */
  .slogan {
    position: absolute; left: 300px; width: 450px; text-align: center;
    font-family: "Roboto Slab", "Rockwell", serif; font-weight: 900; color: var(--white);
    text-shadow: 2px 2px 0 var(--royal), 4px 4px 0 var(--ink);
    letter-spacing: 1.5px; line-height: 1; white-space: nowrap;
  }
  .slogan-top { top: 98px; font-size: 58px; }
  .slogan-bottom { top: 160px; font-size: 48px; }

  /* Right column */
  .headline {
    position: absolute; left: 770px; top: 30px;
    font-family: "Roboto Slab", "Rockwell", serif; font-weight: 900; line-height: 1;
  }
  .headline-main { color: var(--white); font-size: 31px; }
  .headline-sub { color: var(--sky); font-size: 28px; margin-top: 2px; }
  .rule { position: absolute; left: 770px; width: 248px; height: 1px; background: var(--rule); }
  .rule-top { top: 99px; }
  .rule-bottom { top: 218px; }
  .community {
    position: absolute; left: 770px; top: 114px; width: 250px;
    color: var(--white); font-size: 14.5px; line-height: 1.3; font-weight: 400;
  }
  .since-pill {
    position: absolute; left: 770px; top: 162px; width: 198px; height: 36px; border-radius: 18px;
    background: var(--royal); color: var(--white);
    font-weight: 600; font-size: 20px; letter-spacing: 3px;
    display: flex; align-items: center; justify-content: center;
  }
  .phone {
    position: absolute; left: 768px; top: 230px; display: flex; align-items: center; gap: 6px;
    color: var(--white); font-family: "Roboto", sans-serif; font-weight: 700; font-size: 33px; line-height: 1;
  }
  .phone-icon { width: 26px; height: 26px; }
  .address {
    position: absolute; left: 770px; top: 274px; color: var(--white);
    font-size: 11.5px; font-weight: 600; white-space: nowrap;
  }
</style>
</head>
<body>
  <section class="banner">
    <div class="navy-field"></div>
    <div class="reveal" role="img" aria-label="Torn paper opening revealing a red background"></div>

    <div class="brand">
      <span class="brand-dot"></span>
      <div class="brand-text">
        <span class="brand-name">Crestwell<br>Prints Co</span>
        <span class="brand-est">Est. 2009</span>
      </div>
    </div>

    <div class="social">
      <span class="social-dot"></span>
      <span>Follow us <span class="social-handle">@crestwellprints</span></span>
    </div>

    <div class="order-bar">
      <span class="order-label">ORDER TODAY</span>
      <span class="order-url">www.crestwellprintsco.com</span>
    </div>

    <div class="slogan slogan-top">SIGNS</div>
    <div class="slogan slogan-bottom">SHIRTS,SWAG</div>

    <div class="headline">
      <div class="headline-main">WE DO MORE</div>
      <div class="headline-sub">THAN BANNERS</div>
    </div>
    <div class="rule rule-top"></div>
    <p class="community">Producing signage for the Fernmoor Ridge community</p>
    <div class="since-pill">SINCE 2009</div>
    <div class="rule rule-bottom"></div>

    <div class="phone">
      <svg class="phone-icon" viewBox="0 0 26 26" aria-hidden="true">
        <circle cx="13" cy="13" r="12" fill="#a9c6dc"/>
        <path d="M9 7c1 0 2 2.5 2 3s-1 1-1 1.5 2 3.5 4 4.5c.5 0 1-1 1.5-1s3 1 3 2-1.5 2-2.5 2C11 19 7 14 7 9.5 7 8 8 7 9 7z" fill="#163766"/>
      </svg>
      <span>(555) 014-2290</span>
    </div>
    <p class="address">418 harlow lane, ste 12, dallas, TX, 75231</p>
  </section>
</body>
</html>
```